Looking for a dynamic business card for a pizzeria.

A business card with our food, logo, and space for name, title, email, website, phone. The card should convey quality, unique, amazing. On the front, I envision food photo or photos with the owners names and contact information. On the back, more food with locations, website, facebook, twitter, instagram icons. It should look polished, not cartoonish, or plain.
Target Market(s)
upscale, local food buyers, 30-50 years in age.
Industry/Entity Type
Restaurant
Contact Information for Business Card
Business Name: Crustelli, LLC
Website: www.crustelli-example.com
Back:
2 locations: (can list on the back of card)
1. Harborview
3807 Marlow Street
Larkfield, WA 98011
360-555-0143
2. Cedar Ridge
1736 Quenby Street
Larkfield, WA 98014
360-555-0187
front:
EDITABLE space for
Business name
Person's Name
title
2nd title
Email address
cell-phone number
Requirements
Must have
- logo
- my food photo or photos (no watermarks showing)
- locations on back
- Person contact information on front
- full bleed

```html
<!DOCTYPE html>
<html lang="en">
<head>
<meta charset="utf-8">
<title>Crustelli Business Card</title>
<link href="https://fonts.googleapis.com/css2?family=Montserrat:wght@400;500;600;700&display=swap" rel="stylesheet">
<style>
:root{
  --page:#e9e6e2;
  --red:#c9302e;
  --red-light:#d9403a;
  --red-dark:#a3201f;
  --white:#ffffff;
  --green:#2e6a3c;
  --photo-veg:#7c8a4a;
  --photo-meat:#6b4134;
  --photo-dough:#cbb79a;
  --photo-pizza:#c9694b;
}
*{margin:0;padding:0;box-sizing:border-box}
html,body{width:1200px;height:1000px;overflow:hidden;background:var(--page)}
body{position:relative;font-family:"Montserrat",sans-serif;color:var(--white)}
.card{position:absolute;left:265px;width:666px;height:397px;overflow:hidden;background:var(--red);box-shadow:0 3px 10px rgba(0,0,0,.25)}
.card--front{top:73px}
.card--back{top:533px}
.card-art{position:absolute;inset:0;width:100%;height:100%}
.info{position:absolute;right:33px;text-align:right;line-height:1.2}
.person-name{font-size:22px;font-weight:700}
.person-title{font-size:15px;font-weight:400;margin-top:2px}
.company{font-size:16px;font-weight:600;margin-top:30px}
.contact-list{list-style:none;margin-top:10px;font-size:15px}
.contact-list li{height:25px;display:flex;justify-content:flex-end;align-items:center;gap:6px}
.contact-list b{font-weight:700}
.icon{width:14px;height:14px;flex:none}
.wordmark{position:absolute;font-weight:600;letter-spacing:1px;line-height:1}
.wordmark--front{left:32px;top:70px;font-size:38px;color:var(--green)}
.wordmark--back{right:33px;top:46px;font-size:38px;color:var(--white)}
.location-name{font-size:18px;font-weight:700;line-height:22px}
.location-line{font-size:16px;line-height:21px;margin-top:2px}
.location-phone{font-size:16px;line-height:21px;margin-top:6px;display:flex;justify-content:flex-end;align-items:center;gap:6px}
.location + .location{margin-top:11px}
.website{font-size:17px;margin-top:9px}
.social{position:absolute;left:272px;top:340px;display:flex;gap:11px}
.social span{width:22px;height:22px;border-radius:50%;background:var(--white)}
</style>
</head>
<body>

<section class="card card--front">
  <svg class="card-art" viewBox="0 0 666 397">
    <defs>
      <radialGradient id="burst-front" cx="0.75" cy="0.45" r="0.7">
        <stop offset="0" stop-color="var(--red-light)"/>
        <stop offset="1" stop-color="var(--red)"/>
      </radialGradient>
      <linearGradient id="food-front" x1="0" y1="0" x2="1" y2="1">
        <stop offset="0" stop-color="var(--photo-veg)"/>
        <stop offset="0.6" stop-color="var(--photo-meat)"/>
        <stop offset="1" stop-color="#b9744f"/>
      </linearGradient>
    </defs>
    <rect width="666" height="397" fill="url(#burst-front)"/>
    <path d="M0,0 H475 C492,120 420,190 400,255 C382,320 352,360 332,397 H0 Z" fill="var(--red-dark)"/>
    <path role="img" aria-label="Photo collage of a grilled sandwich, pizza rolls and a steak and pepper pizza" d="M0,0 H455 C472,120 400,180 380,250 C362,320 332,360 312,397 H0 Z" fill="url(#food-front)"/>
    <ellipse cx="150" cy="55" rx="185" ry="145" fill="var(--red)"/>
    <ellipse cx="150" cy="52" rx="178" ry="138" fill="var(--white)"/>
  </svg>
  <div class="wordmark wordmark--front">CRUSTELLI</div>
  <div class="info" style="top:96px">
    <div class="person-name">Jordan Vale</div>
    <div class="person-title">Owner / Manager</div>
    <div class="company">Crustelli, LLC</div>
    <ul class="contact-list">
      <li>+ 999 999 9999
        <svg class="icon" viewBox="0 0 14 14"><rect x="4" y="1" width="6" height="12" rx="1" fill="none" stroke="#fff" stroke-width="1.3"/><rect x="5.5" y="3" width="3" height="5" fill="#fff"/></svg></li>
      <li>+ 999 999 9999
        <svg class="icon" viewBox="0 0 14 14"><path d="M1 6 Q7 1 13 6 L11 7 L9 5 H5 L3 7 Z" fill="#fff"/><rect x="3" y="8" width="8" height="4" rx="1" fill="#fff"/></svg></li>
      <li>info@crustelli-example.com
        <svg class="icon" viewBox="0 0 14 14"><rect x="1" y="3" width="12" height="8" fill="#fff"/><path d="M1 3 L7 8 L13 3" fill="none" stroke="var(--red)" stroke-width="1.2"/></svg></li>
      <li><span>www.<b>crustelli-example</b>.com</span>
        <svg class="icon" viewBox="0 0 14 14"><circle cx="7" cy="7" r="6" fill="#fff"/><path d="M4 5 Q6 4 7 6 Q6 8 8 9 Q9 11 7 12" fill="none" stroke="var(--red)" stroke-width="1.2"/></svg></li>
    </ul>
  </div>
</section>

<section class="card card--back">
  <svg class="card-art" viewBox="0 0 666 397">
    <defs>
      <radialGradient id="burst-back" cx="0.8" cy="0.3" r="0.75">
        <stop offset="0" stop-color="var(--red-light)"/>
        <stop offset="1" stop-color="var(--red)"/>
      </radialGradient>
      <linearGradient id="food-dough" x1="0" y1="0" x2="1" y2="0">
        <stop offset="0" stop-color="#6e6a66"/>
        <stop offset="0.4" stop-color="var(--photo-dough)"/>
        <stop offset="1" stop-color="#d8b8a0"/>
      </linearGradient>
      <linearGradient id="food-pizza" x1="0" y1="0" x2="1" y2="1">
        <stop offset="0" stop-color="var(--photo-pizza)"/>
        <stop offset="1" stop-color="#e3cfb4"/>
      </linearGradient>
    </defs>
    <rect width="666" height="397" fill="url(#burst-back)"/>
    <path d="M0,0 H395 C360,120 330,150 295,230 C275,290 270,340 262,397 H0 Z" fill="var(--red-dark)"/>
    <path role="img" aria-label="Photo of hands stretching pizza dough dusted with flour" d="M0,0 H378 C350,80 330,150 318,192 H0 Z" fill="url(#food-dough)"/>
    <path role="img" aria-label="Photo of an uncooked pepperoni pizza with cheese" d="M0,192 H318 C290,250 262,320 245,397 H0 Z" fill="url(#food-pizza)"/>
  </svg>
  <div class="wordmark wordmark--back">CRUSTELLI</div>
  <div class="info" style="top:141px">
    <div class="location">
      <div class="location-name">Harborview</div>
      <div class="location-line">3807 Marlow Street</div>
      <div class="location-line">Larkfield, WA 98011</div>
      <div class="location-phone">360-555-0143
        <svg class="icon" viewBox="0 0 14 14"><path d="M3 1 L5 1 L6 4 L4.5 5.5 Q6 8.5 8.5 9.5 L10 8 L13 9 L13 11 Q12 13 10 13 Q3 11 1 4 Q1 2 3 1 Z" fill="#fff"/></svg></div>
    </div>
    <div class="location">
      <div class="location-name">Cedar Ridge</div>
      <div class="location-line">1736 Quenby Street</div>
      <div class="location-line">Larkfield, WA 98014</div>
      <div class="location-phone">360-555-0187
        <svg class="icon" viewBox="0 0 14 14"><path d="M3 1 L5 1 L6 4 L4.5 5.5 Q6 8.5 8.5 9.5 L10 8 L13 9 L13 11 Q12 13 10 13 Q3 11 1 4 Q1 2 3 1 Z" fill="#fff"/></svg></div>
    </div>
    <div class="website">www.crustelli-example.com</div>
  </div>
  <div class="social" aria-label="Social media links"><span></span><span></span><span></span></div>
</section>

</body>
</html>
```